Fresh Rally Quest

I need a design for and advertisement on a Screen at a Doctor's Surgery. The ad would be up for 15 seconds then on a rotation which last 10 minutes. So every 10 minutes if you are sitting in the Doctor's waiting room you will see my ad for 15 seconds.

I am a Personal Trainer and my company is TrueForm Habits. I need this advertisement for my January promotion, I will be running the ad in December. So I need the ad to send to the agent by this Friday.

I attach something for you to start with, basically person sitting in the doctor's waiting room must see headline, value of offer discounted price and webpage. The rest of the stuff should be on ad for those sitting in the waiting room for a long time.

This is a really important ad as January is the biggest month for Personal Trainers, I can't mess this up

Reason: So I've decided it makes sense to split the project into two, one for the screen, and then the full ad as you have it to fit on an A6 post card. So here are some update: Phone number should be written as (07482) 315907 Change spelling of Program to Programme (£600 Value) change to (Value £600) (£25) Value change to (Value £25) (£45 Value) change to (Value £45) For the screen replace the woman with my picture Also I just got this width to height ratio of the screen is 16:9 The important things to call out on the screen "Early Bird Offer Custom Kick Start Program" "Who Wants To Lose 15 Pounds and Be Healthy in 2015" The Cost of £200 The Savings of £470 The Expiration Date Limited to Fist 10 Individuals Enroll Now The screen should also tell people to pick up a flyer in the Waiting Room Then the flyer, remember just A6 post card should have the full Ad Thank you for taking the time to design my ad

Use colors in my logo. Important for the screen: So I've decided it makes sense to split the project into two, one for the screen, and then the full ad as you have it to fit on an A6 post card. So here are some update: Phone number should be written as (07482) 315907 Change spelling of Program to Programme (£600 Value) change to (Value £600) (£25) Value change to (Value £25) (£45 Value) change to (Value £45) For the screen replace the woman with my picture Also I just got this width to height ratio of the screen is 16:9 The important things to call out on the screen "Early Bird Offer Custom Kick Start Program" "Who Wants To Lose 15 Pounds and Be Healthy in 2015" Cost of £200 Savings of £470 The Expiration Date Limited to First 10 Individuals Enroll Now The screen should also tell people to pick up a flyer in the Waiting Room Then the flyer, remember just A6 post card should have the full Ad Thank you for taking the time to design my ad

Women in the age group of 25 to 60, who want to get strong and fit, but are afraid of the weight room. So measure about strength must be subtle or just not there at all. This is not a call for bodybuilders

• Use colors in my logo. Important for the screen:

So I've decided it makes sense to split the project into two, one for the screen, and then the full ad as you have it to fit on an A6 post card.

So here are some update:

Phone number should be written as (07482) 315907
Change spelling of Program to Programme
(£600 Value) change to (Value £600)
(£25) Value change to (Value £25)
(£45 Value) change to (Value £45)
For the screen replace the woman with my picture

Also I just got this width to height ratio of the screen is 16:9

The important things to call out on the screen
"Early Bird Offer Custom Kick Start Program"
"Who Wants To Lose 15 Pounds and Be Healthy in 2015"
The Cost of £200
The Savings of £470
The Expiration Date
Limited to Fist 10 Individuals
Enroll Now

The screen should also tell people to pick up a flyer in the Waiting Room

Then the flyer, remember just A6 post card should have the full Ad

Thank you for taking the time to design my ad

```html
<!DOCTYPE html>
<html lang="en">
<head>
<meta charset="utf-8">
<title>TrueForm Habits – Early Bird Offer</title>
<link href="https://fonts.googleapis.com/css2?family=Oswald:wght@500&family=Roboto+Slab:wght@400;700&family=Roboto:wght@700&family=Tinos&display=swap" rel="stylesheet">
<style>
  :root {
    --sky: #1e9ad6;
    --sky-light: #5fb3e4;
    --navy: #1c3a6e;
    --navy-glow: #2a78bf;
    --red: #e0262b;
    --charcoal: #3a3a3a;
    --ink: #222;
    --yellow: #f5ea1c;
    --white: #fff;
    --backdrop: #ececec;
  }
  * { box-sizing: border-box; margin: 0; padding: 0; }
  html, body { width: 1200px; height: 701px; overflow: hidden; background: var(--backdrop); }
  .ad {
    position: absolute; left: 10px; top: 17px; width: 1180px; height: 667px;
    background: var(--white); overflow: hidden;
    font-family: "Roboto Slab", Georgia, serif;
  }
  .abs { position: absolute; }

  .trainer-photo {
    left: 4px; top: 5px; width: 316px; height: 316px;
    border: 4px solid var(--red);
    background: radial-gradient(circle at 55% 45%, #a6735a 0 28%, #4a4a4a 45%, #8a8a8a 100%);
  }
  .value-badge {
    left: 50px; top: 286px; width: 198px; height: 198px; border-radius: 50%;
    background: var(--charcoal);
  }
  .value-badge .inner {
    position: absolute; left: 19px; top: 19px; width: 160px; height: 160px; border-radius: 50%;
    background: var(--red); color: var(--white);
    display: flex; align-items: center; justify-content: center; text-align: center;
    font-size: 25px; line-height: 1.3;
  }

  .brand {
    left: 343px; top: 30px; width: 300px;
    font-weight: 700; font-size: 42px; line-height: 1.05; color: var(--charcoal);
  }
  .flyer-note {
    left: 343px; top: 112px; width: 330px;
    font-weight: 700; font-size: 15px; line-height: 20px; color: var(--red);
  }

  .offer-tag {
    left: 693px; top: 11px; width: 467px; height: 109px; border-radius: 20px;
    background: var(--sky); color: var(--white);
    font-family: "Oswald", "Arial Narrow", sans-serif; font-weight: 500;
    font-size: 31px; line-height: 40px; text-align: center;
    display: flex; flex-direction: column; justify-content: center;
  }

  .pitch-panel {
    left: 339px; top: 141px; width: 819px; height: 303px; border-radius: 10px;
    background: radial-gradient(ellipse at 50% 60%, var(--navy-glow) 0%, var(--navy) 70%);
  }
  .headline {
    left: 339px; top: 155px; width: 819px; text-align: center;
    color: var(--white); font-weight: 700; font-size: 25px;
  }
  .headline .year { color: var(--yellow); }

  .price-disc {
    width: 164px; height: 164px; border-radius: 50%; top: 208px;
    color: var(--white); font-weight: 700; text-align: center;
    display: flex; flex-direction: column; justify-content: center;
    font-size: 29px; line-height: 1.25;
  }
  .price-disc .amount { font-size: 36px; }
  .price-disc.cost { left: 391px; background: var(--sky); }
  .price-disc.savings { left: 942px; background: var(--red); }

  .expiry {
    left: 557px; top: 238px; width: 384px; text-align: center;
    color: var(--yellow); font-weight: 700; font-size: 21px;
  }
  .limit-pill {
    left: 557px; top: 272px; width: 384px; height: 35px;
    background: var(--white); border-radius: 0 18px 18px 0;
    color: var(--ink); font-size: 21px; line-height: 35px; padding-left: 52px;
  }
  .limit-pill svg { position: absolute; left: 4px; top: 3px; }

  .phone {
    left: 557px; top: 331px; width: 384px; text-align: center;
    color: var(--white); font-size: 24px;
    display: flex; align-items: center; justify-content: center; gap: 8px;
  }

  .enroll {
    left: 655px; top: 384px; width: 178px; height: 45px; border-radius: 7px;
    background: var(--charcoal); color: var(--white);
    font-weight: 700; font-size: 25px; text-align: center; line-height: 45px;
  }

  .includes-band { left: 0; top: 451px; width: 1180px; height: 216px; background: var(--sky); }
  .includes-tab {
    left: 0; top: 451px; width: 598px; height: 47px;
    background: #111; border-radius: 0 24px 24px 0;
    color: var(--white); font-size: 26px; line-height: 47px; padding-left: 93px;
  }
  .includes-tab svg { position: absolute; left: 0; top: 0; }
  .includes-list {
    left: 22px; top: 508px; list-style: none;
    color: var(--white); font-family: "Tinos", "Times New Roman", serif;
    font-size: 26px; line-height: 36px;
  }
  .includes-list li::before { content: "• "; }

  .jump-figure {
    left: 842px; top: 459px; width: 122px; height: 206px;
    background: var(--sky-light); border-radius: 40px 40px 10px 10px; opacity: .7;
  }

  .save-box {
    left: 980px; top: 457px; width: 190px; height: 206px;
    background: var(--charcoal); color: var(--white);
    font-family: "Roboto", Arial, sans-serif; font-weight: 700;
    font-size: 58px; line-height: 74px; text-align: center;
    display: flex; flex-direction: column; justify-content: center;
  }
</style>
</head>
<body>
  <main class="ad">
    <div class="abs trainer-photo" role="img" aria-label="Portrait of the personal trainer smiling in the gym"></div>

    <div class="abs value-badge">
      <div class="inner">A £670<br>Value for<br>ONLY £200</div>
    </div>

    <div class="abs brand">TrueForm<br>Habits</div>
    <p class="abs flyer-note">Pick up a flyer in the Waiting Room</p>

    <div class="abs offer-tag">
      <span>EARLY BIRD OFFER</span>
      <span>CUSTOM KICKSTART PROGRAMME</span>
    </div>

    <section class="abs pitch-panel"></section>
    <h1 class="abs headline">WHO WANTS TO LOSE 15 POUNDS &amp; BE HEALTHY IN <span class="year">2015</span>?</h1>

    <div class="abs price-disc cost"><span>The</span><span>Cost of</span><span class="amount">£200</span></div>
    <div class="abs price-disc savings"><span>The</span><span>Savings of</span><span class="amount">£470</span></div>

    <p class="abs expiry">Offer Expires 31/12/14</p>
    <p class="abs limit-pill">
      <svg width="40" height="30" viewBox="0 0 40 30" aria-hidden="true" fill="#1c3a6e">
        <rect x="0" y="0" width="7" height="7"/><rect x="10" y="0" width="7" height="7"/><rect x="20" y="0" width="7" height="7"/>
        <rect x="30" y="0" width="7" height="7"/><rect x="20" y="10" width="7" height="7"/><rect x="30" y="10" width="7" height="7"/>
        <rect x="10" y="20" width="7" height="7"/><rect x="20" y="20" width="7" height="7"/>
      </svg>
      Limited to First 10 Individuals
    </p>

    <p class="abs phone">
      <svg width="28" height="28" viewBox="0 0 28 28" aria-hidden="true">
        <circle cx="14" cy="14" r="12.5" fill="none" stroke="#fff" stroke-width="1.6"/>
        <path d="M10 7c-1.5 1-2 3-1 5.5s3.5 6 6 7.5c2 1 3.5.5 4.5-.5l-2.2-2.6-2 1c-1.5-.8-3.3-3-4-4.5l1.4-1.7z" fill="#fff"/>
      </svg>
      (07482) 315907
    </p>

    <div class="abs enroll">Enroll Now</div>

    <section class="abs includes-band"></section>
    <div class="abs includes-tab">
      <svg width="84" height="47" viewBox="0 0 84 47" aria-hidden="true" fill="#1e9ad6">
        <rect x="0" y="2" width="12" height="12"/><rect x="16" y="2" width="12" height="12"/><rect x="32" y="2" width="12" height="12"/><rect x="48" y="2" width="12" height="12"/><rect x="64" y="2" width="12" height="12"/>
        <rect x="0" y="18" width="12" height="12"/><rect x="16" y="18" width="12" height="12"/><rect x="32" y="18" width="12" height="12"/><rect x="48" y="18" width="12" height="12"/><rect x="64" y="18" width="12" height="12"/>
        <rect x="0" y="34" width="12" height="12"/><rect x="16" y="34" width="12" height="12"/><rect x="32" y="34" width="12" height="12"/><rect x="48" y="34" width="12" height="12"/>
      </svg>
      Your KICKSTART Programme&nbsp; Includes:
    </div>
    <ul class="abs includes-list">
      <li>12 Fat-Blasting Training Sessionwith a Personal Trainer (Value £600)</li>
      <li>Exercise Program Specifically Designed to Meet Your Goals (Value £25)</li>
      <li>Unlimited E-mail Coaching (Priceless)</li>
      <li>Done-For-You Meal Plan (Value £45)</li>
    </ul>

    <div class="abs jump-figure" role="img" aria-label="Light blue silhouette of a person jumping with arms raised"></div>

    <div class="abs save-box"><span>Save</span><span>£470</span></div>
  </main>
</body>
</html>
```